Quillmen Letterhead

I would like to create a letterhead file similar to what we have but in MS Word format. Right now this is a PDF and is not functional

```html
<!DOCTYPE html>
<html lang="en">
<head>
<meta charset="UTF-8">
<title>Quillmen Hockey Club Letterhead</title>
<link rel="stylesheet" href="https://fonts.googleapis.com/css2?family=Oswald:wght@500;700&family=Raleway:wght@400;500&display=swap">
<style>
  :root {
    --navy: #0d0f3b;
    --gold: #fdb71a;
    --paper: #ffffff;
    --backdrop: #e9e9e9;
    --white: #ffffff;
  }
  * { margin: 0; padding: 0; box-sizing: border-box; }
  html, body {
    width: 1200px; height: 874px; overflow: hidden;
    background: var(--backdrop);
  }
  .letterhead {
    position: absolute;
    left: 280px; top: 22px;
    width: 640px; height: 830px;
    background: var(--paper);
    box-shadow: 0 4px 18px rgba(0,0,0,0.12);
    overflow: hidden;
  }
  .header-band {
    position: absolute; left: 0; top: 0;
    width: 100%; height: 92px;
    background: var(--navy);
  }
  .accent-top {
    position: absolute; left: 22px; top: 0;
    width: 34px; height: 118px;
    background: var(--gold);
  }
  .club-mark {
    position: absolute; left: 78px; top: 30px;
    display: flex; align-items: center; gap: 6px;
    font-family: "Oswald", sans-serif; font-weight: 700;
    font-size: 20px; letter-spacing: 0.5px;
    color: var(--gold);
  }
  .club-mark .dot {
    width: 10px; height: 10px; border-radius: 50%;
    background: var(--gold);
  }
  .club-name {
    position: absolute; left: 196px; top: 26px;
    color: var(--white);
  }
  .club-name h1 {
    font-family: "Oswald", sans-serif; font-weight: 700;
    font-size: 17px; letter-spacing: 0.4px; line-height: 1.1;
  }
  .club-name p {
    font-family: "Raleway", sans-serif; font-weight: 500;
    font-size: 10px; letter-spacing: 1px; margin-top: 2px;
    margin-left: 12px;
  }
  .contact-list {
    position: absolute; right: 22px; top: 18px;
    list-style: none;
    font-family: "Raleway", sans-serif; font-weight: 400;
    font-size: 9px; color: var(--white);
  }
  .contact-list li {
    display: flex; justify-content: flex-end; align-items: center;
    gap: 5px; margin-bottom: 5px;
  }
  .contact-list svg { width: 10px; height: 10px; flex: none; }
  .footer-band {
    position: absolute; left: 0; bottom: 0;
    width: 100%; height: 20px;
    background: var(--navy);
  }
  .accent-bottom {
    position: absolute; right: 22px; bottom: 12px;
    width: 34px; height: 44px;
    background: var(--gold);
  }
</style>
</head>
<body>
  <div class="letterhead">
    <div class="header-band"></div>
    <div class="accent-top"></div>

    <div class="club-mark"><span class="dot"></span>QUILLMEN</div>

    <div class="club-name">
      <h1>QUILLMEN HOCKEY CLUB</h1>
      <p>ELMCREST</p>
    </div>

    <ul class="contact-list">
      <li>555-014-0192
        <svg viewBox="0 0 10 10"><circle cx="5" cy="5" r="5" fill="#fdb71a"/><path d="M3.3 2.8l1 1-.5.6a3 3 0 0 0 1.8 1.8l.6-.5 1 1-.6.7c-2 0-3.9-1.9-3.9-3.9z" fill="#0d0f3b"/></svg>
      </li>
      <li>elmcrestquillmen.ca
        <svg viewBox="0 0 10 10"><circle cx="5" cy="5" r="5" fill="#fdb71a"/><circle cx="5" cy="5" r="2.4" fill="none" stroke="#0d0f3b" stroke-width="0.8"/><path d="M2.6 5h4.8M5 2.6v4.8" stroke="#0d0f3b" stroke-width="0.6"/></svg>
      </li>
      <li>42 Harrow Road, Elmcrest AB
        <svg viewBox="0 0 10 10"><circle cx="5" cy="5" r="5" fill="#fdb71a"/><path d="M5 8L3.2 5.2a2 2 0 1 1 3.6 0z" fill="#0d0f3b"/><circle cx="5" cy="4.3" r="0.7" fill="#fdb71a"/></svg>
      </li>
    </ul>

    <div class="footer-band"></div>
    <div class="accent-bottom"></div>
  </div>
</body>
</html>
```